Etiketten-Design für Getränkedose
Zielgruppe
Ich werde Getränke in Dosen 250 ml herstellen lassen, welches ich im Markt vertreiben möchte.
Aufgabenstellung
Das Pfandlogo und die EAN müssen an die Etiketten rangebracht werden, deshalb ist es wichtig, dass wenn Sie keine Möglichkeit haben die EAN ranzubringen, dass Platz im Design frei gehalten wird.
Im Anhang 1 finden Sie die Abmessungen von den Etiketten die an die Dosen rangebracht werden sollen!
Das Design muss innerhalb von diesen Abmessungen erstellt werden.
Es handelt sich hier nur um eine Druckvorlage!
Für so eine Druckvorlage muss auf den Etiketten Platz frei gehalten werden.
Ich benötige von Ihnen 3D Dosendesigns, sowie in meiner Skizze.
Wichtig: Es sollen auschließlich die Farben Weiß und Grün genutzt werden.
Meine Marke heißt ' Silver Plum' und es ist wichtig, dass die Farbe grün mit der Limette von meinem Logo passt.
Anhang 2&3= Mein Logo
Anhang 4= Eine Skizze von mir.
Ganz oben am Dosenrand soll das Wort Plum in Grün NICHT mit eingeführt werden.
Ganz unten soll bitte in Farbe Grau die Zahl: (2018) auf Römisch hinzugefügt werden und das Grau und die Schrift soll bitte mit meinem Logo passen:
MMXVIII
Wichtig: Es soll ein edles und modernes Design werden!
Ich freue mich auf Ihre kreativen Designs.
Als Vorgabe: Die Dose soll weiß sein und es sollen grüne Farben benutzt werden und es soll mit dem Logo farblich übereinstimmen.
Vielen Dank im Voraus

```html
<!DOCTYPE html>
<html lang="de">
<head>
<meta charset="UTF-8">
<title>Silver Plum – Dosenetikett 250 ml</title>
<link rel="stylesheet" href="https://fonts.googleapis.com/css2?family=Jura:wght@500&display=swap">
<style>
  :root {
    --label-white: #ffffff;
    --sheen-grey: #e6e8e6;
    --green-light: #c9e6b4;
    --green-mid: #7cc35a;
    --green-deep: #4fa83a;
    --brand-grey: #4a4a4a;
    --year-grey: #7d7d7d;
    --page-bg: #ffffff;
  }

  * { margin: 0; padding: 0; box-sizing: border-box; }

  html, body {
    width: 748px;
    height: 1200px;
    overflow: hidden;
    background: var(--page-bg);
  }

  .can-label {
    position: relative;
    width: 748px;
    height: 1200px;
    overflow: hidden;
    background:
      linear-gradient(90deg,
        rgba(0,0,0,0) 0%, rgba(210,214,210,0.35) 12%, rgba(0,0,0,0) 22%,
        rgba(200,204,200,0.25) 38%, rgba(0,0,0,0) 50%,
        rgba(205,210,205,0.3) 66%, rgba(0,0,0,0) 78%,
        rgba(210,214,210,0.35) 90%, rgba(0,0,0,0) 100%),
      linear-gradient(180deg,
        var(--label-white) 0%,
        var(--label-white) 45%,
        var(--green-light) 68%,
        var(--green-mid) 88%,
        var(--green-deep) 100%);
  }

  .brand {
    position: absolute;
    top: 330px;
    left: 0;
    width: 100%;
    display: flex;
    justify-content: center;
    align-items: center;
    gap: 18px;
  }

  .brand-name {
    font-family: "Jura", sans-serif;
    font-weight: 500;
    font-size: 74px;
    line-height: 1.05;
    letter-spacing: 0.14em;
    text-transform: uppercase;
    color: var(--brand-grey);
    text-align: left;
  }

  .brand-dot {
    width: 92px;
    height: 92px;
    border-radius: 50%;
    background: var(--green-mid);
    flex-shrink: 0;
  }

  .vintage-year {
    position: absolute;
    top: 1010px;
    left: 0;
    width: 100%;
    text-align: center;
    font-family: "Jura", sans-serif;
    font-weight: 500;
    font-size: 26px;
    letter-spacing: 0.22em;
    color: var(--year-grey);
  }

  .base-band {
    position: absolute;
    left: 0;
    bottom: 0;
    width: 100%;
    height: 48px;
    background: var(--green-deep);
  }
</style>
</head>
<body>
  <main class="can-label">
    <div class="brand">
      <p class="brand-name">Silver<br>Plum</p>
      <span class="brand-dot" aria-hidden="true"></span>
    </div>
    <p class="vintage-year">MMXVIII</p>
    <div class="base-band"></div>
  </main>
</body>
</html>
```